Edible Insect Sticker packaging design

The successful designer for this product will be hired again for more packaging design products in this product range.
We are a company that manufactures edible insects and we have some new products coming out we ned packaging for. As you can imagine the stickers are very small 50mm x 50mm.
Each sticker design will be in a set  of 2 (one for the front and one for the back of the packaging).
The front will contain the weight of the product (in grams) as well as the name of the product and design.
The back will contain our company logo and info as well as NIP (Nutritional Information Panel), ingredient declaration, and 3-4 lines of information about how edible insects are great for the environment.
At this stage I would like the packaging to have a slightly environmental free, but still colourful and eye catching. I am open to any suggestions for the design though if you have some great ideas!
Must also contain the slogan (on front or back), "Are you Brave Enough?"
There are several products in the range, and would like the labels to be in a set. Basic lay out will be the same for each product, and the front sticker will be slightly different.
Products are
Zip-A-Dee Crumble- a fly shaped chocolate that contains coconut and fly pupae
Toasty Hoppers- 5 x roasted crickets
Nibbly Grublets- 5 x roasted mealworms
Cocoa Dipped Beasties- 5 x insects, chocolate coated in milk, white or dark chocolate. Insects include crickets, mealworms and fly pupae
Specific information (eg, NIP, ingredients etc) will be sent to chosen designer to add to the deisgn.
Attached is image of 3 products (Zip-A-Dee Crumble, roasted mealworms and roasted crickets) as well as logo. The chocolate coated bugs are the 2 types of roasted bugs pictured in the attachment coated in chocolate.

Updates
Design can be square or round 

Reason: Several designers have asked for an extension to submit new/ revised designs.

Reason: I have extended the deadline by one day to allow for revisions and new designs to be submitted.

Industry/Entity Type
It Company
Look and feel
Each slider illustrates characteristics of the customer's brand and the style your logo design should communicate.

```html
<!DOCTYPE html>
<html lang="en">
<head>
<meta charset="utf-8">
<title>Toasty Hoppers – Sticker Set</title>
<link href="https://fonts.googleapis.com/css2?family=Chewy&family=Short+Stack&family=Kalam:wght@700&display=swap" rel="stylesheet">
<style>
  :root {
    --page: #ffffff;
    --sticker: #ffffff;
    --frame: #e2bd8a;
    --frame-dot: #f3e2c8;
    --olive: #807a12;
    --olive-light: #8f9a2a;
    --rust: #c23a16;
    --brown: #8a2a10;
    --leaf: #8ab33a;
    --ink: #1a1a1a;
    --shadow: rgba(0,0,0,0.28);
  }
  * { box-sizing: border-box; margin: 0; padding: 0; }
  html, body { width: 1200px; height: 810px; overflow: hidden; background: var(--page); }
  .canvas { position: relative; width: 1200px; height: 810px; }

  .sticker {
    position: absolute; top: 197px; width: 416px; height: 399px;
    background: var(--sticker); border-radius: 38px;
    box-shadow: 0 3px 8px var(--shadow), 0 0 1px rgba(0,0,0,0.35);
  }
  .sticker--front { left: 93px; }
  .sticker--back { left: 699px; }

  .frame {
    position: absolute; left: 40px; top: 36px; width: 336px; height: 327px;
    border: 9px solid var(--frame);
  }
  .frame__dot {
    position: absolute; width: 17px; height: 17px; border-radius: 50%;
    background: var(--frame-dot); border: 3px solid var(--frame);
  }
  .frame__dot--tl { left: -13px; top: -13px; }
  .frame__dot--tr { right: -13px; top: -13px; }
  .frame__dot--bl { left: -13px; bottom: -13px; }
  .frame__dot--br { right: -13px; bottom: -13px; }

  .product-name {
    position: absolute; left: 0; right: 0; top: 84px; text-align: center;
    font-family: "Chewy", cursive; font-size: 38px; letter-spacing: 1px;
    color: var(--olive);
  }
  .product-art {
    position: absolute; left: 77px; top: 133px; width: 230px; height: 150px;
    border-radius: 50%;
    background: radial-gradient(ellipse at 60% 45%, #9b6a3c 0%, #c9c98a 35%, #b8e48a 65%, rgba(255,255,255,0) 72%);
  }
  .product-desc {
    position: absolute; left: 0; right: 0; top: 288px; text-align: center;
    font-family: "Short Stack", cursive; font-size: 19px; color: var(--rust);
  }
  .product-weight {
    position: absolute; left: 0; right: 0; top: 316px; text-align: center;
    font-family: "Short Stack", cursive; font-size: 19px; color: var(--olive-light);
  }

  .brand {
    position: absolute; left: 85px; top: 60px; display: flex; align-items: center; gap: 10px;
  }
  .brand__name {
    font-family: "Chewy", cursive; font-size: 27px; line-height: 27px; color: var(--leaf);
    text-align: center;
  }
  .brand__dot { width: 22px; height: 22px; border-radius: 50%; background: var(--leaf); }

  .slogan {
    position: absolute; left: 99px; top: 169px; width: 245px; height: 34px;
    border: 3px solid var(--ink); border-radius: 17px;
    display: flex; align-items: center; justify-content: center;
    font-family: "Kalam", cursive; font-weight: 700; font-size: 17px; color: var(--ink);
  }
  .eco-fact {
    position: absolute; left: 74px; top: 232px; width: 160px; text-align: center;
    font-family: "Kalam", cursive; font-weight: 700; font-size: 18px; line-height: 28px;
    color: var(--brown);
  }

  .nutrition {
    position: absolute; left: 256px; top: 232px; width: 89px; height: 107px;
    border: 1px solid var(--ink); padding: 2px 3px;
    font-family: Arial, Helvetica, sans-serif; color: var(--ink);
  }
  .nutrition__title { font-size: 9px; font-weight: 700; line-height: 10px; border-bottom: 3px solid var(--ink); }
  .nutrition__row {
    display: flex; justify-content: space-between;
    font-size: 4.5px; line-height: 5.6px; border-bottom: 0.5px solid var(--ink);
  }
  .nutrition__row--indent span:first-child { padding-left: 4px; }
  .nutrition__row--thick { border-bottom: 2px solid var(--ink); }
  .nutrition__note { font-size: 4px; line-height: 5px; margin-top: 1px; }
</style>
</head>
<body>
<main class="canvas">

  <section class="sticker sticker--front">
    <div class="frame">
      <span class="frame__dot frame__dot--tl"></span><span class="frame__dot frame__dot--tr"></span>
      <span class="frame__dot frame__dot--bl"></span><span class="frame__dot frame__dot--br"></span>
    </div>
    <h1 class="product-name">Toasty Hoppers</h1>
    <div class="product-art" role="img" aria-label="Illustration of a roasted cricket on grass inside a swirling ring"></div>
    <p class="product-desc">5 x roasted crickets</p>
    <p class="product-weight">20g</p>
  </section>

  <section class="sticker sticker--back">
    <div class="frame">
      <span class="frame__dot frame__dot--tl"></span><span class="frame__dot frame__dot--tr"></span>
      <span class="frame__dot frame__dot--bl"></span><span class="frame__dot frame__dot--br"></span>
    </div>
    <div class="brand">
      <p class="brand__name">Critter<br>Pantry</p>
      <span class="brand__dot"></span>
    </div>
    <p class="slogan">"Are you Brave Enough?"</p>
    <p class="eco-fact">Insects reproduce at a faster rate than beef animals</p>

    <div class="nutrition">
      <p class="nutrition__title">Nutrition Facts</p>
      <div class="nutrition__row"><span>Serving Size 20g</span></div>
      <div class="nutrition__row nutrition__row--thick"><span>Amount Per Serving</span></div>
      <div class="nutrition__row"><span>Calories 95</span></div>
      <div class="nutrition__row"><span>Total Fat 3g</span><span>5%</span></div>
      <div class="nutrition__row nutrition__row--indent"><span>Saturated Fat 1g</span></div>
      <div class="nutrition__row nutrition__row--indent"><span>Trans Fat 0g</span></div>
      <div class="nutrition__row"><span>Cholesterol 0mg</span><span>0%</span></div>
      <div class="nutrition__row"><span>Sodium 5mg</span><span>0%</span></div>
      <div class="nutrition__row"><span>Total Carbohydrate 1g</span><span>0%</span></div>
      <div class="nutrition__row nutrition__row--indent"><span>Dietary Fiber 1g</span></div>
      <div class="nutrition__row nutrition__row--thick"><span>Protein 13g</span></div>
      <div class="nutrition__row"><span>Iron 10%</span><span>Calcium 4%</span></div>
      <p class="nutrition__note">Daily values based on 2,000 calories.</p>
    </div>
  </section>

</main>
</body>
</html>
```